Health & Wellness Contest - The Bright Harvest Renewal

We need a postcard design that is professional and grabs the attention of people who see it. The postcard will be left in fitness centers and posted on social media. The front of the card MUST look amazing - make potential participants want to pick it up and find out more information; the back of the card will have the contest details. The goal is to have people sign up for a 90 day fitness program, and most of the marketing will be with this postcard.

Target Market(s)

People that are thinking about beginning a health regiment; people who are already used to exercising and are willing to try a new supplement

Industry/Entity Type

Health And Wellness

Colors

Designer to choose colors to be used in the design.

Requirements
Must have
• Front Cover -- Must have the phrase "The Bright Harvest Renewal" and must have "$2,500 Grand Prize"; and must have "BrightHarvestRenewal.com"
Nice to have
• Design on Front; Details on Back; appeal to both men and women

```html
<!DOCTYPE html>
<html lang="en">
<head>
<meta charset="utf-8">
<title>The Bright Harvest Renewal – Postcard</title>
<link href="https://fonts.googleapis.com/css2?family=Marcellus&family=Signika:wght@400;500;600&family=Open+Sans:wght@400;600;700&display=swap" rel="stylesheet">
<style>
  :root{
    --page:#ececec;
    --teal:#0fa3bb;
    --teal-light:#41c4d9;
    --teal-ink:#0a95ad;
    --gold:#f2b917;
    --gold-deep:#e0a50c;
    --white:#ffffff;
    --stamp:#cfcfcf;
  }
  *{margin:0;padding:0;box-sizing:border-box}
  html,body{width:949px;height:1200px;overflow:hidden;background:var(--page)}
  body{position:relative;font-family:"Open Sans",sans-serif;color:var(--white)}

  .postcard{position:absolute;left:125px;width:632px;height:489px;overflow:hidden;
    box-shadow:0 6px 14px rgba(0,0,0,.25)}
  .postcard--front{top:82px;background:linear-gradient(135deg,var(--teal) 0%,var(--teal-light) 55%,var(--teal) 100%)}
  .postcard--back{top:625px;background:var(--white)}

  .layer{position:absolute;inset:0;width:632px;height:489px}

  .title{position:absolute;font-family:"Marcellus",serif;font-weight:400;text-align:center;line-height:1;color:var(--white)}
  .title__lead{display:block;font-size:31px}
  .title__main{display:block;font-size:42px;margin-top:14px;letter-spacing:.5px}

  .divider{position:absolute;height:2px;background:var(--white)}
  .divider::after{content:"";position:absolute;left:50%;top:-2px;width:5px;height:5px;margin-left:-2.5px;border-radius:50%;background:var(--white)}

  .mission{position:absolute;font-size:12px;line-height:16px;text-align:center}

  .join-band{position:absolute;left:0;top:196px;width:318px;height:64px;background:var(--white);
    color:var(--teal-ink);font-family:"Signika",sans-serif;font-size:13.5px;line-height:17px;text-align:center;padding-top:7px}

  .benefits{position:absolute;top:287px;list-style:none;font-family:"Signika",sans-serif;font-size:12.5px;line-height:19.6px}
  .benefits li{display:flex;align-items:center;gap:6px}
  .benefits svg{width:10px;height:10px;flex:none}

  .deadline{position:absolute;background:var(--gold);border:2px solid var(--white);border-radius:26px;
    font-size:14.5px;line-height:18px;color:var(--white)}

  .prize{position:absolute;width:112px;height:112px}
  .prize__text{position:absolute;inset:0;display:flex;flex-direction:column;align-items:center;justify-content:center;text-align:center}
  .prize__label{font-size:11px}
  .prize__amount{font-family:"Signika",sans-serif;font-size:20px;font-weight:600;letter-spacing:-.6px;margin-top:1px}

  .site{position:absolute;text-align:center}
  .site b{font-weight:700}

  .stamp-box{position:absolute;left:512px;top:31px;width:101px;height:48px;border:2px solid var(--stamp)}

  .signup{position:absolute;left:31px;top:330px;font-family:"Marcellus",serif;font-size:40px;color:var(--white)}
  .url-band{position:absolute;left:0;top:403px;width:362px;height:37px;background:var(--white);
    color:var(--teal-ink);font-size:18px;text-align:center;line-height:37px}
  .url-band b{font-weight:700}
  .sponsor-note{position:absolute;left:0;top:441px;width:362px;text-align:center;font-size:12px;line-height:16px}
</style>
</head>
<body>

<!-- FRONT -->
<section class="postcard postcard--front">
  <svg class="layer" role="img" aria-label="Photo of a smiling woman in white workout clothes crouching over a glass bathroom scale on a wooden floor" viewBox="0 0 632 489">
    <defs>
      <linearGradient id="frontPhoto" x1="0" y1="0" x2="0" y2="1">
        <stop offset="0" stop-color="#f4f1ec"/>
        <stop offset=".55" stop-color="#e7ddd2"/>
        <stop offset="1" stop-color="#c89a66"/>
      </linearGradient>
    </defs>
    <path d="M420,0 C360,150 330,350 318,489 L632,489 L632,0 Z" fill="url(#frontPhoto)"/>
  </svg>
  <svg class="layer" aria-hidden="true" viewBox="0 0 632 489">
    <path d="M392,0 C338,150 304,340 296,489 L312,489 C322,350 356,150 414,0 Z" fill="var(--gold)"/>
    <path d="M420,0 C360,150 330,350 318,489" fill="none" stroke="var(--white)" stroke-width="4"/>
  </svg>

  <h1 class="title" style="left:10px;top:34px;width:300px">
    <span class="title__lead">The Bright Harvest</span>
    <span class="title__main">RENEWAL</span>
  </h1>
  <div class="divider" style="left:35px;top:136px;width:250px"></div>
  <p class="mission" style="left:10px;top:149px;width:300px">The Bright Harvest Renewal has one mission<br>to help people be a better version of themselves.</p>

  <p class="join-band">Join us in the Bright Harvest Renewal<br>and experience some of the benefits that<br>countless others have seen:</p>

  <ul class="benefits" style="left:20px">
    <li><svg viewBox="0 0 10 10"><circle cx="5" cy="5" r="4.2" fill="none" stroke="var(--gold)" stroke-width="1.2"/><path d="M3 5.2l1.5 1.4L7.2 3.6" fill="none" stroke="var(--gold)" stroke-width="1.2"/></svg>Better health</li>
    <li><svg viewBox="0 0 10 10"><circle cx="5" cy="5" r="4.2" fill="none" stroke="var(--gold)" stroke-width="1.2"/><path d="M3 5.2l1.5 1.4L7.2 3.6" fill="none" stroke="var(--gold)" stroke-width="1.2"/></svg>Appetite suppression</li>
    <li><svg viewBox="0 0 10 10"><circle cx="5" cy="5" r="4.2" fill="none" stroke="var(--gold)" stroke-width="1.2"/><path d="M3 5.2l1.5 1.4L7.2 3.6" fill="none" stroke="var(--gold)" stroke-width="1.2"/></svg>Better energy</li>
    <li><svg viewBox="0 0 10 10"><circle cx="5" cy="5" r="4.2" fill="none" stroke="var(--gold)" stroke-width="1.2"/><path d="M3 5.2l1.5 1.4L7.2 3.6" fill="none" stroke="var(--gold)" stroke-width="1.2"/></svg>Fat Loss</li>
    <li><svg viewBox="0 0 10 10"><circle cx="5" cy="5" r="4.2" fill="none" stroke="var(--gold)" stroke-width="1.2"/><path d="M3 5.2l1.5 1.4L7.2 3.6" fill="none" stroke="var(--gold)" stroke-width="1.2"/></svg>Better focus</li>
  </ul>
  <ul class="benefits" style="left:156px">
    <li><svg viewBox="0 0 10 10"><circle cx="5" cy="5" r="4.2" fill="none" stroke="var(--gold)" stroke-width="1.2"/><path d="M3 5.2l1.5 1.4L7.2 3.6" fill="none" stroke="var(--gold)" stroke-width="1.2"/></svg>Increased awareness</li>
    <li><svg viewBox="0 0 10 10"><circle cx="5" cy="5" r="4.2" fill="none" stroke="var(--gold)" stroke-width="1.2"/><path d="M3 5.2l1.5 1.4L7.2 3.6" fill="none" stroke="var(--gold)" stroke-width="1.2"/></svg>Better mood</li>
    <li><svg viewBox="0 0 10 10"><circle cx="5" cy="5" r="4.2" fill="none" stroke="var(--gold)" stroke-width="1.2"/><path d="M3 5.2l1.5 1.4L7.2 3.6" fill="none" stroke="var(--gold)" stroke-width="1.2"/></svg>Muscle preservation</li>
    <li><svg viewBox="0 0 10 10"><circle cx="5" cy="5" r="4.2" fill="none" stroke="var(--gold)" stroke-width="1.2"/><path d="M3 5.2l1.5 1.4L7.2 3.6" fill="none" stroke="var(--gold)" stroke-width="1.2"/></svg>Better sleep</li>
    <li><svg viewBox="0 0 10 10"><circle cx="5" cy="5" r="4.2" fill="none" stroke="var(--gold)" stroke-width="1.2"/><path d="M3 5.2l1.5 1.4L7.2 3.6" fill="none" stroke="var(--gold)" stroke-width="1.2"/></svg>And much more...</li>
  </ul>

  <p class="deadline" style="left:14px;top:395px;width:400px;height:51px;padding:14px 0 0 25px">Challenge Deadline: Register by October 31, 2017.</p>

  <div class="prize" style="left:383px;top:363px">
    <svg viewBox="0 0 112 112" aria-hidden="true" width="112" height="112">
      <circle cx="56" cy="56" r="54" fill="var(--gold)" stroke="var(--gold)" stroke-width="3" stroke-dasharray="3 2.6"/>
      <circle cx="56" cy="56" r="48" fill="var(--white)"/>
      <circle cx="56" cy="56" r="44" fill="var(--gold)"/>
    </svg>
    <div class="prize__text"><span class="prize__label">Grand Prize</span><span class="prize__amount">$2,500.00</span></div>
  </div>

  <p class="site" style="left:0;top:454px;width:296px;font-size:12px">www.<b>BrightHarvestRenewal</b>.com</p>
</section>

<!-- BACK -->
<section class="postcard postcard--back">
  <svg class="layer" viewBox="0 0 632 489" role="img" aria-label="Photo of the toned torsos of a man and a woman in workout clothes">
    <defs>
      <linearGradient id="backTeal" x1="0" y1="0" x2="1" y2="1">
        <stop offset="0" stop-color="var(--teal)"/>
        <stop offset=".5" stop-color="var(--teal-light)"/>
        <stop offset="1" stop-color="var(--teal)"/>
      </linearGradient>
      <linearGradient id="backPhoto" x1="0" y1="0" x2="1" y2="0">
        <stop offset="0" stop-color="#c98f6c"/>
        <stop offset=".5" stop-color="#b27b5c"/>
        <stop offset="1" stop-color="#d6a07c"/>
      </linearGradient>
      <clipPath id="tealArea">
        <path d="M0,0 L262,0 C305,120 345,260 360,489 L0,489 Z"/>
      </clipPath>
    </defs>
    <path d="M0,0 L262,0 C305,120 345,260 360,489 L0,489 Z" fill="url(#backTeal)"/>
    <rect x="97" y="254" width="270" height="149" fill="url(#backPhoto)" opacity=".85" clip-path="url(#tealArea)"/>
    <path d="M262,0 L286,0 C328,130 365,280 378,489 L360,489 C345,260 305,120 262,0 Z" fill="var(--gold)"/>
  </svg>

  <h2 class="title" style="left:0;top:30px;width:320px">
    <span class="title__lead">The Bright Harvest</span>
    <span class="title__main">RENEWAL</span>
  </h2>
  <div class="divider" style="left:29px;top:134px;width:254px"></div>
  <p class="mission" style="left:0;top:146px;width:312px">The Bright Harvest Renewal has one mission<br>to help people be a better version of themselves.</p>

  <p class="deadline" style="left:19px;top:202px;width:300px;height:52px;padding:6px 0 0 28px">Challenge Deadline:<br>Register by October 31, 2017.</p>

  <div class="prize" style="left:291px;top:175px">
    <svg viewBox="0 0 112 112" aria-hidden="true" width="112" height="112">
      <circle cx="56" cy="56" r="54" fill="var(--gold)" stroke="var(--gold)" stroke-width="3" stroke-dasharray="3 2.6"/>
      <circle cx="56" cy="56" r="48" fill="var(--white)"/>
      <circle cx="56" cy="56" r="44" fill="var(--gold)"/>
    </svg>
    <div class="prize__text"><span class="prize__label">Grand Prize</span><span class="prize__amount">$2,500.00</span></div>
  </div>

  <p class="signup">sign up</p>

  <p class="url-band">www.<b>BrightHarvestRenewal</b>.com</p>
  <p class="sponsor-note">For Challenge details, email one of our sponsors at<br>Info@MaplewoodCounsel.org</p>

  <div class="stamp-box"></div>
</section>

</body>
</html>
```